Personal Motivational Quote Poster Design

I would like to create a poster with some of my favorite quotes to hang in my office. I did similar projects in 2012 and 2014. I've uploaded the winning designs so you can get a better idea of what I'm looking for. I will provide feedback on your design within 24 hours of receiving it.

The poster must contain the following quotes:

“What the pupil must learn, if he learns anything at all, is that the world will do most of the work for you, provided you cooperate with it by identifying how it really works and aligning with those realities. If we do not let the world teach us, it teaches us a lesson.” - Walter Brindley

“I tackle every big new problem by asking two questions: Who has dealt with this problem well? And what can we learn from them?” - Hal Porter

“If we can really understand the problem, the answer will come out of it, because the answer is not separate from the problem.” - Ravel Ondashanti

“Success is nothing more than a few simple disciplines, practiced every day; while failure is simply a few errors in judgment, repeated every day. It is the accumulative weight of our disciplines and our judgments that leads us to either fortune or failure.” - Ned Calve

“Inaction breeds doubt and fear. Action breeds confidence and courage.” - Rex Halloway

“What’s the one thing you can do, such that by doing it, everything else will be easier or unnecessary?” - Lyle Danvers

Requirements
Must have
• The poster will be 24" high x 36" long and printed on canvas, so the image you create needs to have a resolution of at least 2700 x 3900.
Nice to have
• I don't have an exact vision for how the poster should look, so I am totally open to you using your creativity to develop, arrange and present the content as you'd like.

That said, I would like an image (photo or posterized image) of the person being quoted along with each quote. I do not have specific images that I would like you to use, so you will need to find the images on your own.

The images don't need to be perfect... I am more interested in the poster relating the essence of the quotes and the people being quoted than I am in perfect photographic images of the people being quoted.

```html
<!DOCTYPE html>
<html lang="en">
<head>
<meta charset="utf-8">
<title>Quote Poster</title>
<link href="https://fonts.googleapis.com/css2?family=Delius&display=swap" rel="stylesheet">
<style>
  :root {
    --ink: #141414;
    --paper: #ffffff;
    --peach: #f7c6aa;
    --tan: #e5d1b9;
    --clay: #d3bca7;
    --mist: #dcdcdc;
    --sage: #e3efd4;
    --photo-light: rgba(225,225,225,0.95);
    --photo-mid: rgba(185,185,185,0.9);
  }
  html, body { margin: 0; padding: 0; overflow: hidden; background: var(--paper); }
  .poster {
    position: relative;
    width: 1200px; height: 800px;
    overflow: hidden;
    background: var(--paper);
    font-family: "Delius", "Comic Sans MS", cursive;
    color: var(--ink);
  }
  .abs { position: absolute; box-sizing: border-box; }
  .poster-frame { left: 14px; top: 14px; width: 1172px; height: 772px; border: 7px solid var(--ink); }

  .fill-peach { left: 38px; top: 23px; width: 206px; height: 707px; background: var(--peach); }
  .fill-tan { left: 243px; top: 196px; width: 205px; height: 360px; background: var(--tan); }
  .fill-clay { left: 633px; top: 97px; width: 168px; height: 681px; background: var(--clay); }
  .fill-mist { left: 767px; top: 33px; width: 256px; height: 523px; background: var(--mist); }
  .fill-sage { left: 1023px; top: 57px; width: 157px; height: 705px; background: var(--sage); }

  .portrait { border-radius: 46% 46% 4px 4px / 30% 30% 4px 4px; }
  .portrait-brindley { left: 38px; top: 590px; width: 190px; height: 140px; background: linear-gradient(180deg, rgba(214,150,125,0.2), rgba(200,140,118,0.85)); }
  .portrait-porter { left: 228px; top: 565px; width: 210px; height: 187px; background: linear-gradient(180deg, var(--photo-light), var(--photo-mid)); }
  .portrait-ondashanti { left: 440px; top: 565px; width: 195px; height: 187px; background: linear-gradient(180deg, rgba(232,232,232,0.9), rgba(196,196,196,0.9)); }
  .portrait-halloway { left: 636px; top: 565px; width: 165px; height: 190px; background: linear-gradient(180deg, rgba(190,165,145,0.5), rgba(165,140,122,0.9)); }
  .portrait-calve { left: 805px; top: 590px; width: 215px; height: 162px; background: linear-gradient(180deg, var(--photo-light), var(--photo-mid)); }
  .portrait-danvers { left: 1028px; top: 560px; width: 152px; height: 200px; background: linear-gradient(180deg, rgba(200,212,190,0.6), rgba(110,120,110,0.9)); }

  .frame { border: 2.5px solid var(--ink); }
  .frame-brindley { left: 34px; top: 34px; width: 197px; height: 719px; }
  .frame-porter { left: 225px; top: 187px; width: 216px; height: 355px; }
  .frame-ondashanti { left: 422px; top: 110px; width: 216px; height: 643px; }
  .frame-halloway { left: 621px; top: 87px; width: 165px; height: 467px; }
  .frame-calve { left: 772px; top: 35px; width: 254px; height: 718px; border-width: 3.5px; }
  .frame-danvers { left: 1019px; top: 58px; width: 148px; height: 487px; }

  .mark { font-size: 30px; line-height: 1; font-style: italic; }
  .quote { text-align: center; font-size: 19px; line-height: 26.5px; white-space: nowrap; }
  .big { font-size: 29px; line-height: 1; }
  .huge { font-size: 30px; line-height: 36px; }
  .inline-huge { font-size: 30px; line-height: 1; }
  .author { font-size: 15px; white-space: nowrap; transform: translateX(-50%); }
</style>
</head>
<body>
<main class="poster">
  <div class="abs poster-frame"></div>

  <div class="abs fill-peach"></div>
  <div class="abs fill-tan"></div>
  <div class="abs fill-clay"></div>
  <div class="abs fill-mist"></div>
  <div class="abs fill-sage"></div>

  <div class="abs portrait portrait-brindley" role="img" aria-label="Posterized portrait of Walter Brindley"></div>
  <div class="abs portrait portrait-porter" role="img" aria-label="Greyscale portrait of Hal Porter"></div>
  <div class="abs portrait portrait-ondashanti" role="img" aria-label="Greyscale portrait of Ravel Ondashanti"></div>
  <div class="abs portrait portrait-halloway" role="img" aria-label="Sepia portrait of Rex Halloway"></div>
  <div class="abs portrait portrait-calve" role="img" aria-label="Greyscale portrait of Ned Calve"></div>
  <div class="abs portrait portrait-danvers" role="img" aria-label="Tinted portrait of Lyle Danvers"></div>

  <div class="abs frame frame-brindley"></div>
  <div class="abs frame frame-porter"></div>
  <div class="abs frame frame-ondashanti"></div>
  <div class="abs frame frame-halloway"></div>
  <div class="abs frame frame-calve"></div>
  <div class="abs frame frame-danvers"></div>

  <!-- Walter Brindley -->
  <div class="abs mark" style="left:47px;top:46px;">“</div>
  <div class="abs quote" style="left:43px;top:74px;width:180px;">
    &nbsp;&nbsp;&nbsp;What the pupil<br>must learn, if he<br>learns anything at<br>all, is that the<br>world will do<br>most of the work<br>for you, provided<br>you cooperate<br>with it by<br>identifying how it<br>really works and<br>aligning with<br>those realities.
    <div class="huge" style="margin-top:4px;">If we do not<br>let the world<br>teach us, it<br>teaches us a<br>lesson.”</div>
  </div>
  <div class="abs author" style="left:136px;top:640px;">– Walter Brindley</div>

  <!-- Hal Porter -->
  <div class="abs mark" style="left:256px;top:222px;">“</div>
  <div class="abs quote" style="left:240px;top:250px;width:180px;">
    &nbsp;&nbsp;&nbsp;I tackle every<br>big new problem<br>by asking two<br>questions:<br><span class="big">Who</span> has dealt<br>with this problem<br>well? And <span class="big">what</span><br>can we learn from<br>them?”
  </div>
  <div class="abs author" style="left:334px;top:549px;">– Hal Porter</div>

  <!-- Ravel Ondashanti -->
  <div class="abs mark" style="left:448px;top:134px;">“</div>
  <div class="abs quote" style="left:441px;top:158px;width:180px;">
    &nbsp;&nbsp;&nbsp;If we can really<br>understand the<br>problem, the<br>answer will come<br>out of it, because<br>the
    <div class="huge" style="margin-top:4px;">answer is<br>not separate<br>from the<br>problem.”</div>
  </div>
  <div class="abs author" style="left:533px;top:510px;">– Ravel Ondashanti</div>

  <!-- Rex Halloway -->
  <div class="abs mark" style="left:700px;top:158px;">“</div>
  <div class="abs quote" style="left:626px;top:212px;width:158px;">
    <div class="huge">Inaction</div>breeds doubt<br>and fear.
    <div class="huge" style="margin-top:6px;">Action</div>breeds<br>confidence<br>and courage.”
  </div>
  <div class="abs author" style="left:707px;top:482px;">– Rex Halloway</div>

  <!-- Ned Calve -->
  <div class="abs mark" style="left:844px;top:66px;">“</div>
  <div class="abs quote" style="left:809px;top:80px;width:180px;">
    <div class="huge" style="margin-left:30px;margin-bottom:8px;">Success</div>
    is nothing more<br>than a few simple<br>disciplines, practiced<br>every day; while<br><span class="inline-huge">failure</span> is simply a<br>few errors in<br>judgment, repeated<br>every day.<br>It is the<br>accumulative weight<br>of our disciplines<br>and our judgments<br>that leads us to<br>either fortune or<br>failure.”
  </div>
  <div class="abs author" style="left:903px;top:578px;">– Ned Calve</div>

  <!-- Lyle Danvers -->
  <div class="abs mark" style="left:1063px;top:134px;">“</div>
  <div class="abs quote" style="left:1018px;top:158px;width:150px;">
    &nbsp;&nbsp;&nbsp;&nbsp;What’s
    <div class="huge">the one<br>thing<br>you can<br>do,</div>
    such that by<br>doing it,<br>everything<br>else will be<br>easier or<br>unnecessary?<br>”
  </div>
  <div class="abs author" style="left:1110px;top:562px;">– Lyle Danvers</div>
</main>
</body>
</html>
```